Design for Marketing Consulting Agency - Please see attachments

Looking for a very simple site - 3-5 pages, one with a portfolio page to showcase our work where we can leave comments on it. Looking for modern/clean/impactful design to represent our brand. Here is example of what I like: https://www.trelvon.com/en-us/ logo and mood board and copy for website (minus the portfolio). Prefer black/gray/white with pops of color/imagery that come from the logo. Prefer dark hero, more white and pops of the orange and red for the rest of the site.

Target Market(s)

Small to medium size businesses

Font styles to use
Sans Serif

Colors

Designer to choose only greyscale colors for use in the design.

Requirements
Must have
• Please see mood board. Prefer mostly black/white site with pops of color and imagery.
Nice to have
• Sample portfolio page?
Should not have
• Don't make it look 'futuristic' . Try to make it modern and clean.

```html
<!DOCTYPE html>
<html lang="en">
<head>
<meta charset="utf-8">
<title>Northpeak Marketing</title>
<link href="https://fonts.googleapis.com/css2?family=Comfortaa:wght@400;600;700&family=Poppins:wght@500;600&display=swap" rel="stylesheet">
<style>
:root{
  --dark:#303030;
  --dark-2:#3a3a3a;
  --orange:#f7a823;
  --cream:#fff8ec;
  --grey-bg:#f3f3f3;
  --white:#ffffff;
  --ink:#2b2b2b;
  --muted:#555555;
  --line:#e4e4e4;
}
*{margin:0;padding:0;box-sizing:border-box}
html,body{width:1200px;height:4732px;overflow:hidden}
body{font-family:"Comfortaa",sans-serif;color:var(--ink);background:var(--white);position:relative}
.abs{position:absolute}
section,header,footer{position:absolute;left:0;width:1200px}
.btn{position:absolute;display:flex;align-items:center;justify-content:center;background:var(--orange);color:var(--ink);font-family:"Poppins",sans-serif;font-weight:600;font-size:10.5px;text-transform:uppercase;letter-spacing:.2px;text-decoration:none}
.eyebrow{position:absolute;font-size:12px;color:var(--orange);text-transform:uppercase}
.section-title{position:absolute;font-size:31px;font-weight:700;color:var(--ink)}
.center{left:0;width:1200px;text-align:center}
.ph{position:absolute}

.brand{position:absolute;display:flex;align-items:center;gap:10px}
.brand-mark{width:38px;height:38px;background:var(--orange)}
.brand-name{font-size:14px;font-weight:700;line-height:15px;color:var(--white);text-transform:uppercase}

.hero{top:0;height:676px;background:var(--dark);overflow:hidden}
.nav{position:absolute;top:30px;font-size:11px;color:var(--white);text-transform:uppercase;font-family:"Poppins",sans-serif;font-weight:500}
.nav a{position:absolute;white-space:nowrap;color:inherit;text-decoration:none}
.nav a.active{color:var(--orange)}
.phone{position:absolute;top:27px;left:870px;display:flex;align-items:center;gap:8px;color:var(--white);font-family:"Poppins",sans-serif;font-size:11px;font-weight:500}
.hero-kicker{left:60px;top:186px;color:var(--white);font-size:15px}
.hero-title{left:60px;top:212px;color:var(--white);font-size:33px;font-weight:700;line-height:49px;width:410px}
.hero-title u{text-decoration:underline;text-decoration-color:var(--orange);text-decoration-thickness:4px;text-underline-offset:6px}
.hero-text{left:60px;top:380px;width:375px;color:var(--white);font-size:12.5px;line-height:24px}

.intro{top:676px;height:300px;background:var(--cream)}
.intro p{position:absolute;left:245px;top:108px;width:710px;text-align:center;font-size:14.5px;line-height:26px;color:var(--muted)}

.about{top:976px;height:505px;background:var(--white)}
.about-text{left:630px;top:170px;width:440px;font-size:12.5px;line-height:24px;color:var(--muted)}

.packages{top:1481px;height:801px;background:var(--grey-bg)}
.card{position:absolute;top:175px;width:344px;height:551px;background:var(--white);box-shadow:0 2px 8px rgba(0,0,0,.05)}
.card .ph{left:0;top:0;width:344px;height:232px;border-radius:8px 8px 0 0}
.card h3{position:absolute;left:30px;top:258px;width:300px;font-size:16px;font-weight:700;line-height:26px}
.card h3 span{color:var(--orange)}
.card .meta{position:absolute;left:30px;top:320px;font-size:12px}
.card .meta b{font-weight:700}
.card ul{position:absolute;left:30px;width:300px;list-style:none;font-size:12px;line-height:19px;color:var(--muted)}

.team{top:2282px;height:517px;background:var(--white)}
.team-text{left:60px;top:160px;width:470px;font-size:12px;line-height:24px;color:var(--muted)}

.testimonials{top:2799px;height:542px;background:var(--grey-bg)}
.review{position:absolute;top:174px;width:525px;height:252px;background:var(--white)}
.review .avatar{left:30px;top:31px;width:61px;height:59px;background:linear-gradient(135deg,#c9b7a6,#7d6a5a)}
.review .name{position:absolute;left:111px;top:40px;font-size:16px;font-weight:700;color:var(--orange)}
.review .src{position:absolute;left:111px;top:66px;font-size:11px;color:var(--muted)}
.review .rule{position:absolute;left:30px;right:30px;top:113px;height:1px;background:var(--line)}
.review p{position:absolute;left:30px;top:132px;width:470px;font-size:12px;line-height:24px;color:var(--muted)}
.review p b{color:var(--orange);font-size:30px;font-weight:700;vertical-align:-9px;margin-right:4px;line-height:0}
.dot{position:absolute;top:458px;width:10px;height:10px;border:1px solid #888}
.dot.on{background:var(--orange);border-color:var(--orange)}

.portfolio{top:3341px;height:1073px;background:var(--white)}
.work{position:absolute;width:525px}
.work .ph{position:relative;width:525px;height:330px}
.work h4{margin-top:12px;padding-left:4px;font-size:16px;font-weight:700}

.footer{top:4414px;height:268px;background:var(--dark);color:var(--white)}
.footer h5{position:absolute;top:58px;font-size:16px;font-weight:700;color:var(--orange)}
.footer ul{position:absolute;top:96px;list-style:none;font-size:11px;line-height:26.5px}
.contact-row{position:absolute;left:667px;display:flex;align-items:flex-start;gap:14px;font-size:11px;line-height:16px}
.icon-box{width:30px;height:28px;background:var(--dark-2);display:flex;align-items:center;justify-content:center;flex:none}
.social{position:absolute;top:178px;width:32px;height:32px;background:var(--orange)}
.copyright{top:4682px;height:50px;background:var(--orange);display:flex;align-items:center;justify-content:center;font-size:11px;color:var(--dark)}
.copyright b{font-weight:700}
</style>
</head>
<body>

<section class="hero">
  <div class="brand" style="left:60px;top:18px">
    <span class="brand-mark"></span>
    <span class="brand-name">Northpeak<br>Marketing</span>
  </div>
  <nav class="nav">
    <a class="active" style="left:373px">Home</a>
    <a style="left:450px">Packages</a>
    <a style="left:551px">Portfolio</a>
    <a style="left:656px">About Us</a>
    <a style="left:752px">Contact Us</a>
  </nav>
  <div class="phone">
    <svg width="15" height="15" viewBox="0 0 24 24"><path fill="#f7a823" d="M6.6 10.8a15.1 15.1 0 0 0 6.6 6.6l2.2-2.2a1 1 0 0 1 1-.25 11.4 11.4 0 0 0 3.6.57 1 1 0 0 1 1 1V20a1 1 0 0 1-1 1A17 17 0 0 1 3 4a1 1 0 0 1 1-1h3.5a1 1 0 0 1 1 1c0 1.25.2 2.45.57 3.57a1 1 0 0 1-.25 1z"/></svg>
    (555) 0142 318
  </div>
  <a class="btn" style="left:1020px;top:18px;width:119px;height:37px">Get Started</a>

  <div class="abs hero-kicker">We Deliver</div>
  <h1 class="abs hero-title">Simple, Clear, and Impactful <u>Messaging</u> and <u>Designs.</u></h1>
  <p class="abs hero-text">It's an unfortunate fact – many business owners overthink their marketing. They try to be overly creative or wordy, resulting in empty statements, confused consumers, and lost revenue opportunities.</p>
  <a class="btn" style="left:60px;top:524px;width:120px;height:36px">Get In Touch</a>

  <div class="abs" style="left:735px;top:116px;width:405px;height:460px;background:var(--orange)"></div>
  <div class="ph" role="img" aria-label="Team of three people reviewing work on a laptop at a white desk" style="left:478px;top:118px;width:632px;height:558px;background:linear-gradient(160deg,#8f8a84 0%,#d9d3cb 45%,#f2efea 100%)"></div>
  <div class="abs" style="left:420px;top:612px;width:756px;height:64px;background:#f7f7f7;border-radius:8px 8px 0 0"></div>
</section>

<section class="intro">
  <p>Northpeak Marketing has a simple, thorough process that we use to understand your customer base and their unique pain points. We then develop clear, impactful messaging and beautiful designs that resonate with your audience, differentiate you in your market, and drive sales.</p>
  <svg class="abs" style="left:580px;top:280px" width="40" height="20" viewBox="0 0 40 20"><path d="M2 20a18 18 0 0 1 36 0" fill="none" stroke="#bbb" stroke-width="1"/></svg>
</section>

<section class="about">
  <div class="abs" style="left:116px;top:75px;width:430px;height:357px;border:6px solid var(--orange);border-right:none;border-radius:60px 0 0 60px"></div>
  <div class="ph" role="img" aria-label="Colleagues working at laptops in a bright open-plan office" style="left:126px;top:85px;width:410px;height:337px;border-radius:50px 0 0 50px;background:linear-gradient(180deg,#cfd3d4,#a9aeae 60%,#d8d5cf)"></div>
  <div class="abs" style="left:478px;top:75px;width:68px;height:70px;background:var(--orange)"></div>
  <div class="abs" style="left:357px;top:367px;width:189px;height:65px;background:var(--orange);display:flex;align-items:center;gap:8px;padding-left:6px;color:var(--white)">
    <span style="font-size:46px;font-weight:400;line-height:1">20</span>
    <span style="font-size:13px;font-weight:700;line-height:16px">years of<br>experience</span>
  </div>
  <div class="eyebrow" style="left:630px;top:97px">About Us</div>
  <h2 class="section-title" style="left:630px;top:118px">Who Are We?</h2>
  <p class="abs about-text">Northpeak Marketing is a Marketing Agency that delivers a breadth of services from brand/rebrand, strategy, design, and web to digital and print marketing campaigns and trade shows. We bring over 20 years of experience in marketing for both B2B to B2C organizations ranging from 5M to over 200M. We're passionate. We're poignant. We know what you're trying to say, and so will your customers.</p>
  <a class="btn" style="left:630px;top:375px;width:149px;height:35px">Learn More About</a>
</section>

<section class="packages">
  <div class="eyebrow center" style="top:74px">Services</div>
  <h2 class="section-title center" style="top:100px">Our Packages</h2>

  <article class="card" style="left:60px">
    <div class="ph" role="img" aria-label="Restaurant website and menu mockups on a yellow background" style="background:linear-gradient(135deg,#fde7b8,#f9cf7d)"></div>
    <h3>Website &amp; Messaging Facelift -<br><span>$3000 -$4000</span></h3>
    <div class="meta"><b>Meetings Necessary:</b> 4-5 hours</div>
    <ul style="top:352px"><li><b style="color:var(--ink)">The Output:</b></li><li>~ Two homepage mockups.</li><li>~ One mood board.</li><li>~ Two versions of value proposition<br>&nbsp;&nbsp;&nbsp;messaging ~ x words.</li></ul>
    <a class="btn" style="left:30px;top:485px;width:134px;height:35px">See Case Study</a>
  </article>

  <article class="card" style="left:428px">
    <div class="ph" role="img" aria-label="Business card mockup on a terracotta background" style="background:linear-gradient(135deg,#c9773f,#a9582a)"></div>
    <h3>Simple Brand Rebuild -<br><span>$5000-$6000</span></h3>
    <div class="meta"><b>Meetings Necessary:</b> 6-7 hours</div>
    <ul style="top:352px"><li><b style="color:var(--ink)">The Output:</b></li><li>~ 5 logo concepts</li><li>~ Two homepage mockups</li><li>~ One brand storyboard</li><li>~ Two versions of value proposition<br>messaging</li></ul>
    <a class="btn" style="left:30px;top:485px;width:134px;height:35px">See Case Study</a>
  </article>

  <article class="card" style="left:796px">
    <div class="ph" role="img" aria-label="City street at night lit by colourful billboards" style="background:linear-gradient(160deg,#1d4f5a,#6a2a4d 55%,#1b1b2b)"></div>
    <h3>Additional Services Offered -<br><span>(Charged Hourly)</span></h3>
    <ul style="top:340px"><li>~ Strategic Consulting on Growth<br>&nbsp;&nbsp;&nbsp;Strategies and Building Teams</li><li>~ Trade Show Management &amp; Booth Designs</li><li>~ Email Marketing Campaigns</li><li>~ Digital Marketing Campaigns</li></ul>
    <a class="btn" style="left:30px;top:485px;width:134px;height:35px">See Case Study</a>
  </article>
</section>

<section class="team">
  <div class="eyebrow" style="left:60px;top:75px">Know More</div>
  <h2 class="section-title" style="left:60px;top:102px">Our Team</h2>
  <p class="abs team-text">Northpeak Marketing is run and managed by Dana Whitfield. It has a team of experts from content creation to graphic design and digital marketing. Dana is a passionate marketing visionary with 20+ years of experience leading direct and channel marketing teams and creating powerful and effective multi-channel marketing strategies and campaigns. She has experience working with businesses ranging from 100k to Fortune 500 companies. Dana has her master's degree from Harlow College and her undergraduate degree from Ridgefield University.</p>
  <a class="btn" style="left:60px;top:407px;width:105px;height:36px">Learn More</a>

  <div class="abs" style="left:601px;top:80px;width:528px;height:357px;border:6px solid var(--orange);border-radius:60px 0 0 60px"></div>
  <div class="ph" role="img" aria-label="Grid of six team member portraits" style="left:611px;top:90px;width:512px;height:340px;border-radius:50px 0 0 50px;background:linear-gradient(135deg,#e6e2dd,#c9c3bc);overflow:hidden">
    <svg width="512" height="340"><g stroke="#ffffff" stroke-width="3"><line x1="171" y1="0" x2="171" y2="340"/><line x1="341" y1="0" x2="341" y2="340"/><line x1="0" y1="170" x2="512" y2="170"/></g></svg>
  </div>
</section>

<section class="testimonials">
  <div class="eyebrow center" style="top:76px">Testimonials</div>
  <h2 class="section-title center" style="top:102px">What Happy Clients Say</h2>

  <article class="review" style="left:60px">
    <div class="ph avatar" role="img" aria-label="Client portrait"></div>
    <div class="name">Marcus Reed</div>
    <div class="src">Reviewly Review</div>
    <div class="rule"></div>
    <p><b>“</b>Lorem ipsum dolor sit amet, consectetuer adipiscing elit, sed diam nonummy nibh euismod tincidunt ut laoreet dolore magna aliquam erat volutpat. Ut wisi enim ad minim veniam, quis nostrud exerci tation ullamcorper suscipit lobortis nisl ut aliquip.</p>
  </article>
  <article class="review" style="left:614px">
    <div class="ph avatar" role="img" aria-label="Client portrait"></div>
    <div class="name">Lena Carvallo</div>
    <div class="src">Reviewly Review</div>
    <div class="rule"></div>
    <p><b>“</b>Lorem ipsum dolor sit amet, consectetuer adipiscing elit, sed diam nonummy nibh euismod tincidunt ut laoreet dolore magna aliquam erat volutpat. Ut wisi enim ad minim veniam, quis nostrud exerci tation ullamcorper suscipit lobortis nisl ut aliquip.</p>
  </article>

  <span class="dot" style="left:549px"></span>
  <span class="dot" style="left:572px"></span>
  <span class="dot on" style="left:595px"></span>
  <span class="dot" style="left:618px"></span>
  <span class="dot" style="left:641px"></span>
</section>

<section class="portfolio">
  <div class="eyebrow center" style="top:74px">Portfolio</div>
  <h2 class="section-title center" style="top:100px">Our Work</h2>

  <div class="work" style="left:60px;top:173px">
    <div class="ph" role="img" aria-label="Figure in a spacesuit standing among cars in teal fog" style="background:linear-gradient(180deg,#2f8f96,#1d5a62 60%,#3a2c2a)"></div>
    <h4>Lorem ipsum dolor sit amet</h4>
  </div>
  <div class="work" style="left:614px;top:173px">
    <div class="ph" role="img" aria-label="Building facade covered in greenery" style="background:linear-gradient(160deg,#c9d1d3,#55623f 55%,#2f3a2a)"></div>
    <h4>Lorem ipsum dolor sit amet</h4>
  </div>
  <div class="work" style="left:60px;top:568px">
    <div class="ph" role="img" aria-label="Pink skincare product bottles on a white background" style="background:linear-gradient(135deg,#f1efee,#f3bfd3 55%,#e6e2e0)"></div>
    <h4>Lorem ipsum dolor sit amet</h4>
  </div>
  <div class="work" style="left:614px;top:568px">
    <div class="ph" role="img" aria-label="Aerial view of a city street between tall buildings" style="background:linear-gradient(180deg,#b9c2a9,#3a4438 45%,#1f2420)"></div>
    <h4>Lorem ipsum dolor sit amet</h4>
  </div>

  <a class="btn" style="left:548px;top:963px;width:104px;height:35px">View More</a>
</section>

<footer class="footer">
  <div class="brand" style="left:60px;top:52px">
    <span class="brand-mark"></span>
    <span class="brand-name">Northpeak<br>Marketing</span>
  </div>
  <div class="abs" style="left:60px;top:134px;font-size:15px;font-weight:700">Follow Us On:</div>
  <span class="social" style="left:60px" aria-label="Social profile"></span>
  <span class="social" style="left:101px" aria-label="Social profile"></span>
  <span class="social" style="left:141px" aria-label="Social profile"></span>
  <span class="social" style="left:182px" aria-label="Social profile"></span>

  <h5 style="left:287px">Company</h5>
  <ul style="left:287px"><li>Home</li><li>About Us</li><li>Packages</li><li>Portfolio</li><li>Contact Us</li></ul>

  <h5 style="left:436px">Packages</h5>
  <ul style="left:436px"><li>Website &amp; Messaging Facelift</li><li>Simple Brand Rebuild</li><li>Additional Services</li></ul>

  <h5 style="left:667px">Contact Details</h5>
  <div class="contact-row" style="top:96px">
    <span class="icon-box"><svg width="12" height="16" viewBox="0 0 12 16"><path d="M6 0a6 6 0 0 0-6 6c0 4.5 6 10 6 10s6-5.5 6-10a6 6 0 0 0-6-6zm0 8.5A2.5 2.5 0 1 1 6 3.5a2.5 2.5 0 0 1 0 5z" fill="#f7a823"/></svg></span>
    <span>123 Building Name, Area Name,<br>City, Country - Zipcode</span>
  </div>
  <div class="contact-row" style="top:136px;align-items:center">
    <span class="icon-box"><svg width="14" height="14" viewBox="0 0 24 24"><path fill="#f7a823" d="M6.6 10.8a15.1 15.1 0 0 0 6.6 6.6l2.2-2.2a1 1 0 0 1 1-.25 11.4 11.4 0 0 0 3.6.57 1 1 0 0 1 1 1V20a1 1 0 0 1-1 1A17 17 0 0 1 3 4a1 1 0 0 1 1-1h3.5a1 1 0 0 1 1 1c0 1.250.2 2.45.57 3.57a1 1 0 0 1-.25 1z"/></svg></span>
    <span>(555) 0142 318</span>
  </div>
  <div class="contact-row" style="top:176px;align-items:center">
    <span class="icon-box"><svg width="14" height="11" viewBox="0 0 14 11"><rect width="14" height="11" rx="1" fill="#f7a823"/><path d="M1 1l6 5 6-5" fill="none" stroke="#3a3a3a" stroke-width="1.2"/></svg></span>
    <span style="text-decoration:underline">info@northpeakmark.com</span>
  </div>

  <h5 style="left:952px">Get In Touch</h5>
  <div class="abs" style="left:952px;top:99px;font-size:11px">Contact US Today to Talk To Us!</div>
  <a class="btn" style="left:952px;top:129px;width:112px;height:35px">Contact Us</a>
</footer>

<div class="abs copyright" style="left:0;width:1200px">©&nbsp;<b>NORTHPEAK MARKETING</b>&nbsp;2022. All Rights Reserved.</div>

</body>
</html>
```